Quick & Dirty Poster Design Project - A2 Posters

I run a business called Terra Lumen. We sell high end outdoor flooring and walling (natural stone products) to architects and designers.

We work mainly with high end landscape designers on garden design and outdoor architecture.

Our sales teams provide advice and expertise and sell architectural design products to architects and designers.

I wanted to design some fun A2 posters to put in the sales offices just to create a bit of energy and momentum for staff. These are for internal use only.

The 4 copy lines are:

1.Beware of people who don't get their hands dirty

2. If you don't take a chance you won't have one

3. Having trouble getting started? Quit talking and start doing

4. Remember the questions you ask are more important than anything you could ever say

Just one copy line for each poster

(Pls note due to the limited budget and timings, I'm expecting interesting typeset posters not "designed" artworks). Thanks

Target Market(s)

sales team

Industry/Entity Type

Landscape

Requirements
Must have
• Our logo (Terra Lumen) - I have provided a few versions of the logo
Nice to have
• Some design element alongside the typeface / copy

```html
<!DOCTYPE html>
<html lang="en">
<head>
<meta charset="utf-8">
<title>Terra Lumen – Take a Chance</title>
<link rel="stylesheet" href="https://fonts.googleapis.com/css2?family=Overlock:wght@900&display=swap">
<style>
  :root {
    --page: #ffffff;
    --teal: #017a8d;
    --pink: #e6009b;
    --white: #ffffff;
    --ink: #111111;
    --figure-tone: #3e8f9c;
  }
  html, body {
    margin: 0;
    padding: 0;
    width: 1200px;
    height: 900px;
    overflow: hidden;
    background: var(--page);
  }
  .canvas {
    position: relative;
    width: 1200px;
    height: 900px;
  }
  .poster {
    position: absolute;
    left: 297px;
    top: 20px;
    width: 583px;
    height: 832px;
    background: var(--teal);
    overflow: hidden;
    font-family: "Overlock", "Trebuchet MS", sans-serif;
    font-weight: 900;
  }
  .headline {
    margin: 0;
    position: absolute;
    left: 0;
    top: 0;
    width: 100%;
  }
  .headline span {
    position: absolute;
    display: block;
    white-space: nowrap;
  }
  .line-small {
    color: var(--white);
    font-size: 56px;
    line-height: 1;
  }
  .line-if { left: 72px; top: 46px; }
  .line-have { left: 80px; top: 336px; }
  .line-shout {
    color: var(--pink);
    font-size: 104px;
    line-height: 1;
    text-transform: uppercase;
  }
  .line-take { left: 64px; top: 112px; letter-spacing: 14px; word-spacing: 30px; }
  .line-chance { left: 64px; top: 222px; letter-spacing: 3px; }
  .line-one {
    color: var(--white);
    font-size: 214px;
    line-height: 1;
    left: 64px;
    top: 348px;
    letter-spacing: 2px;
  }
  .illustration {
    position: absolute;
    left: 105px;
    top: 568px;
    width: 360px;
    height: 152px;
    background: linear-gradient(180deg, var(--teal) 0%, var(--figure-tone) 100%);
    border-radius: 8px;
  }
  .ground {
    position: absolute;
    left: 0;
    top: 716px;
    width: 583px;
    height: 10px;
  }
  .brand {
    position: absolute;
    right: 22px;
    bottom: 24px;
    display: flex;
    align-items: center;
    gap: 6px;
    color: var(--white);
    font-size: 17px;
    line-height: 1;
  }
  .brand-dot {
    width: 14px;
    height: 14px;
    border-radius: 50%;
    background: var(--white);
  }
</style>
</head>
<body>
<main class="canvas">
  <section class="poster">
    <h1 class="headline">
      <span class="line-small line-if">If you don't</span>
      <span class="line-shout line-take">Take a</span>
      <span class="line-shout line-chance">Chance</span>
      <span class="line-small line-have">you won't have</span>
      <span class="line-one">one</span>
    </h1>
    <div class="illustration" role="img" aria-label="Cartoon scene: a small character offers a bouquet of pink flowers to a delighted taller character, with a little one and a pink heart beside them"></div>
    <svg class="ground" viewBox="0 0 583 10" aria-hidden="true">
      <path d="M0 5 C 80 3, 160 7, 240 5 S 420 3, 583 5" fill="none" stroke="var(--ink)" stroke-width="2.5"/>
    </svg>
    <div class="brand">
      <span class="brand-dot"></span>
      <span class="brand-name">Terra Lumen</span>
    </div>
  </section>
</main>
</body>
</html>
```